Business Card Design Project

beauty / make up / lashes

Industry/Entity Type

Business

Contact Information for Business Card

pink / gold / wait / black vintage classic elegant design

```html
<!DOCTYPE html>
<html lang="en">
<head>
<meta charset="utf-8">
<title>Velora Lash Studio – Business Cards</title>
<link rel="stylesheet" href="https://fonts.googleapis.com/css2?family=Lato:wght@300;400;700&display=swap">
<style>
  :root {
    --stage: #ece7df;
    --ink: #141414;
    --ink-soft: #2a2a2a;
    --cream: #f7f2e8;
    --cream-deep: #e6d9bf;
    --gold: #d8c39a;
    --gold-light: #efe2c4;
    --gold-dark: #b79d6b;
  }
  * { margin: 0; padding: 0; box-sizing: border-box; }
  html, body {
    width: 1200px; height: 913px; overflow: hidden;
    background: var(--stage);
    font-family: "Lato", sans-serif;
  }
  .canvas { position: relative; width: 1200px; height: 913px; }

  .card {
    position: absolute;
    width: 560px; height: 320px;
    border-radius: 6px;
    overflow: hidden;
    box-shadow: 0 14px 30px rgba(0,0,0,.18);
  }

  /* Front */
  .card-front { left: 70px; top: 90px; }
  .front-pattern {
    position: absolute; inset: 0;
    background: radial-gradient(ellipse at 40% 40%, var(--cream) 0%, var(--cream-deep) 100%);
  }
  .brand-disc {
    position: absolute; left: 50%; top: 50%;
    width: 240px; height: 240px; margin: -120px 0 0 -120px;
    border-radius: 50%;
    background: var(--ink-soft);
    display: flex; align-items: center; justify-content: center;
  }
  .brand-name {
    color: var(--gold);
    font-weight: 400;
    font-size: 26px;
    letter-spacing: 1px;
    text-align: center;
    line-height: 1.3;
  }

  /* Back */
  .card-back {
    left: 570px; top: 480px;
    background: linear-gradient(160deg, #262626 0%, var(--ink) 60%);
    border-bottom: 10px solid var(--gold);
  }
  .holder { position: absolute; top: 40px; width: 100%; text-align: center; color: var(--gold-light); }
  .holder-name { font-size: 28px; font-weight: 700; letter-spacing: 1px; }
  .holder-role { font-size: 15px; font-weight: 300; letter-spacing: 1px; margin-top: 2px; }
  .holder-rule {
    display: block; width: 40px; height: 1px;
    margin: 14px auto 0;
    background: var(--gold);
  }

  .contact-row {
    position: absolute; top: 178px; left: 20px; right: 20px;
    display: flex; justify-content: space-between;
    color: var(--gold-light); font-size: 12px; font-weight: 400;
  }
  .contact-item { display: flex; align-items: center; gap: 6px; white-space: nowrap; }
  .contact-item svg { flex: none; }

  .address-block {
    position: absolute; top: 222px; width: 100%; text-align: center; color: var(--gold-light);
  }
  .address-pin { display: block; margin: 0 auto 4px; }
  .company { font-size: 15px; letter-spacing: 1px; }
  .address { font-size: 12.5px; margin-top: 4px; }
</style>
</head>
<body>
<main class="canvas">

  <section class="card card-front">
    <div class="front-pattern" role="img" aria-label="Cream and gold interlocking arc pattern"></div>
    <div class="brand-disc">
      <p class="brand-name">Velora<br>Lash Studio</p>
    </div>
  </section>

  <section class="card card-back">
    <header class="holder">
      <h1 class="holder-name">Corinne Ashford</h1>
      <p class="holder-role">Managing Director</p>
      <span class="holder-rule"></span>
    </header>

    <div class="contact-row">
      <span class="contact-item">
        <svg width="12" height="12" viewBox="0 0 12 12"><circle cx="6" cy="6" r="5.3" fill="none" stroke="var(--gold)"/><path d="M4 3.5 L5 5 L4.5 5.6 Q5.5 7 6.6 7.5 L7.2 7 L8.6 8 L8 8.8 Q5 8.6 3.3 4.2 Z" fill="var(--gold)"/></svg>
        180 04 27 39
      </span>
      <span class="contact-item">
        <svg width="12" height="12" viewBox="0 0 12 12"><circle cx="6" cy="6" r="5.3" fill="none" stroke="var(--gold)"/><path d="M4 3.5 L5 5 L4.5 5.6 Q5.5 7 6.6 7.5 L7.2 7 L8.6 8 L8 8.8 Q5 8.6 3.3 4.2 Z" fill="var(--gold)"/></svg>
        180 04 27 39
      </span>
      <span class="contact-item">
        <svg width="12" height="12" viewBox="0 0 12 12"><circle cx="6" cy="6" r="5.3" fill="none" stroke="var(--gold)"/><rect x="3" y="4" width="6" height="4" fill="none" stroke="var(--gold)" stroke-width=".8"/><path d="M3 4 L6 6.3 L9 4" fill="none" stroke="var(--gold)" stroke-width=".8"/></svg>
        hello@velorastudio.com
      </span>
      <span class="contact-item">
        <svg width="12" height="12" viewBox="0 0 12 12"><circle cx="6" cy="6" r="5.3" fill="none" stroke="var(--gold)"/><circle cx="6" cy="6" r="2.6" fill="none" stroke="var(--gold)" stroke-width=".8"/><path d="M3.4 6 H8.6" stroke="var(--gold)" stroke-width=".8"/></svg>
        www.velorastudio.com
      </span>
    </div>

    <div class="address-block">
      <svg class="address-pin" width="12" height="12" viewBox="0 0 12 12"><circle cx="6" cy="6" r="5.3" fill="none" stroke="var(--gold)"/><path d="M6 9 Q3.6 6.2 3.9 4.7 A2.1 2.1 0 0 1 8.1 4.7 Q8.4 6.2 6 9 Z" fill="var(--gold)"/></svg>
      <p class="company">VELORA LASH STUDIO</p>
      <p class="address">PO Box 20458 Harbour Lane East, Victoria 8012 Australia</p>
    </div>
  </section>

</main>
</body>
</html>
```